Corporate Brochure Cover Design

We need a design for a corporate A4 Size portfolio cover (front and back) which we will be distributing. to our commercial clients.

We are a professional plumbing company that is an industry leader for service we provide to our clients and technology we use. The design needs to incorporate the colours black, red, white and silver and needs to include our logo. We dont have any slogans or mottos... If you wanted to use something it could be "Delivering exceptional service...Always!" however i dont want it to b the focal point of the cover.

Im looking for something professional and modern that has the WOW factor!

Size is A4 - both front and back covers. You can include pictures as well or sample pictures of where we can source and put our own team pictures.

if you have any questions, please do not hesitate to contact me.

Target Market(s)

Our commercial & strata clients - professional industry.

Industry/Entity Type

Commercial

Font styles to use
Sans Serif

Requirements
Must have
• Red, black, white, silver as the colour scheme.
• Include the logo.
Nice to have
• Modern design and something that makes the client go WOW before they open the brochure.
Should not have
• lots of text

```html
<!DOCTYPE html>
<html lang="en">
<head>
<meta charset="utf-8">
<title>Brochure Cover</title>
<link rel="stylesheet" href="https://fonts.googleapis.com/css2?family=Open+Sans:wght@300;600&family=Oswald:wght@500;600&display=swap">
<style>
  :root {
    --red: #e9474b;
    --black: #1b1b1d;
    --graphite: #3b3b3c;
    --white: #fbf7f2;
    --ink: #1e1a1a;
  }
  html, body {
    margin: 0;
    padding: 0;
    width: 800px;
    height: 1200px;
    overflow: hidden;
    background: var(--red);
  }
  .cover {
    position: relative;
    width: 800px;
    height: 1200px;
    background: var(--red);
    overflow: hidden;
  }
  .top-band {
    position: absolute;
    left: 0;
    top: 0;
    width: 800px;
    height: 315px;
    display: flex;
  }
  .top-band__left {
    width: 400px;
    background: var(--graphite);
  }
  .top-band__right {
    width: 400px;
    background: var(--black);
    display: flex;
    align-items: center;
    justify-content: center;
  }
  .brand {
    display: flex;
    align-items: center;
    gap: 14px;
  }
  .brand__dot {
    width: 20px;
    height: 20px;
    border-radius: 50%;
    background: var(--red);
  }
  .brand__name {
    font-family: "Open Sans", sans-serif;
    font-weight: 600;
    font-size: 38px;
    letter-spacing: 1px;
    color: var(--white);
  }
  .headline {
    position: absolute;
    left: 0;
    width: 800px;
    text-align: center;
    white-space: nowrap;
  }
  .headline__lead {
    top: 420px;
    font-family: "Open Sans", sans-serif;
    font-weight: 300;
    font-size: 80px;
    line-height: 1;
    color: var(--white);
  }
  .headline__figure {
    top: 545px;
    font-family: "Oswald", sans-serif;
    font-weight: 600;
    font-size: 185px;
    line-height: 1;
    letter-spacing: 2px;
    color: var(--white);
    transform: scaleY(1.55);
    transform-origin: top center;
  }
  .headline__caption {
    top: 915px;
    font-family: "Oswald", sans-serif;
    font-weight: 500;
    font-size: 48px;
    line-height: 1;
    letter-spacing: 1px;
    word-spacing: 10px;
    color: var(--ink);
    transform: scaleY(1.2);
    transform-origin: top center;
  }
  .intro {
    position: absolute;
    left: 70px;
    top: 1030px;
    width: 680px;
    margin: 0;
    font-family: "Open Sans", sans-serif;
    font-weight: 300;
    font-size: 21px;
    line-height: 44px;
    color: var(--white);
    white-space: nowrap;
  }
</style>
</head>
<body>
  <main class="cover">
    <header class="top-band">
      <div class="top-band__left"></div>
      <div class="top-band__right">
        <div class="brand">
          <span class="brand__dot"></span>
          <span class="brand__name">CORELINE</span>
        </div>
      </div>
    </header>
    <div class="headline headline__lead">In Excess of</div>
    <div class="headline headline__figure">100,000</div>
    <div class="headline headline__caption">SUCCESSFULLY COMPLETED JOBS</div>
    <p class="intro">We have achieved over 100,000 successfully completed jobs to date.<br>You can trust that we know the best solution for you.</p>
  </main>
</body>
</html>
```